Poster Design Project

Need a design for a music festival called Counter-Lanternweek

The design needs to have areas for the following:
- Band Names
- DJ Names
- Sponsor Names and Logos
- Event location, Date & Time

Industry/Entity Type

Festival

```html
<!DOCTYPE html>
<html lang="en">
<head>
<meta charset="utf-8">
<title>Counter-Lanternweek — Festival Poster</title>
<link rel="stylesheet" href="https://fonts.googleapis.com/css2?family=Audiowide&family=Comfortaa:wght@500;700&family=Saira+Extra+Condensed:wght@700&display=swap">
<style>
  :root {
    --night: #140603;
    --ember: #3a0c04;
    --rust: #8a2a0a;
    --amber: #d8701e;
    --glow: #f0a040;
    --card-red: #c8250e;
    --card-deep: #8e1406;
    --paper: #ffffff;
    --ink: #0a0a0a;
    --steel: #6b6462;
    --steel-edge: #1c1715;
    --strike: #c42a10;
  }
  * { margin: 0; padding: 0; box-sizing: border-box; }
  html, body { width: 848px; height: 1200px; overflow: hidden; background: var(--night); }

  .poster {
    position: relative;
    width: 848px;
    height: 1200px;
    overflow: hidden;
    background: var(--night);
    font-family: "Comfortaa", sans-serif;
  }

  .backdrop {
    position: absolute; inset: 0;
    width: 848px; height: 1200px;
  }

  .instrument-art {
    position: absolute;
    left: 250px; top: 140px;
    width: 598px; height: 900px;
    background:
      radial-gradient(ellipse 40% 30% at 70% 70%, rgba(240,150,50,.55), rgba(150,40,10,.35) 55%, transparent 80%),
      radial-gradient(ellipse 35% 28% at 30% 55%, rgba(220,110,40,.45), rgba(120,30,10,.3) 55%, transparent 80%),
      linear-gradient(180deg, transparent, rgba(60,55,55,.35) 75%, transparent);
  }

  .event-details {
    position: absolute;
    right: 16px; top: 14px;
    font-family: "Audiowide", sans-serif;
    font-size: 40px;
    letter-spacing: 1px;
    color: var(--paper);
    white-space: nowrap;
  }

  .lineup-card {
    position: absolute;
    left: 58px; top: 104px;
    width: 270px; height: 384px;
    transform: rotate(7deg);
    background: linear-gradient(160deg, var(--card-red), var(--card-deep));
    border: 5px solid var(--paper);
    border-radius: 4px;
    padding: 66px 0 0 34px;
    color: var(--paper);
    box-shadow: 0 6px 18px rgba(0,0,0,.45);
  }
  .lineup-card .headliner {
    font-size: 31px; font-weight: 700; line-height: 1.1;
  }
  .lineup-card .support {
    font-size: 22px; font-weight: 700; line-height: 1.45;
  }
  .lineup-card .group + .group { margin-top: 20px; }

  .sponsor-band {
    position: absolute;
    left: 297px; top: 582px;
    width: 551px; height: 266px;
    background: linear-gradient(90deg, rgba(255,255,255,.35), rgba(255,255,255,.6) 30%, rgba(255,255,255,.55));
    display: flex; align-items: center; justify-content: center;
    text-align: center;
    font-size: 54px; font-weight: 500; line-height: 1.45;
    color: var(--ink);
  }

  .title-strip {
    position: absolute;
    left: 0; top: 1000px;
    width: 848px; height: 200px;
    background: linear-gradient(180deg, rgba(10,8,8,.75), var(--night));
  }

  .festival-title {
    position: absolute; left: 0; top: 0;
    width: 848px; height: 1200px;
  }
  .festival-title .prefix {
    font-family: "Comfortaa", sans-serif;
    font-weight: 700;
    font-size: 118px;
    fill: var(--paper);
  }
  .festival-title .name {
    font-family: "Saira Extra Condensed", sans-serif;
    font-weight: 700;
    font-size: 222px;
    fill: var(--steel);
    stroke: var(--steel-edge);
    stroke-width: 4px;
  }
  .festival-title .strike { stroke: var(--strike); stroke-width: 26px; stroke-linecap: butt; }
</style>
</head>
<body>
<main class="poster">
  <svg class="backdrop" viewBox="0 0 848 1200" role="img" aria-label="Collage of guitars, sheet music and an amplifier in warm orange and red tones">
    <defs>
      <linearGradient id="amberBand" x1="0" y1="0" x2="1" y2="1">
        <stop offset="0" stop-color="#e07a22"/>
        <stop offset="1" stop-color="#a83a0c"/>
      </linearGradient>
      <radialGradient id="emberGlow" cx="0.55" cy="0.55" r="0.6">
        <stop offset="0" stop-color="#7a1e08"/>
        <stop offset="1" stop-color="#140603"/>
      </radialGradient>
    </defs>
    <rect width="848" height="1200" fill="url(#emberGlow)"/>
    <polygon points="0,0 560,0 848,180 848,430 0,520" fill="url(#amberBand)" opacity="0.9"/>
    <polygon points="0,520 848,430 848,560 0,700" fill="#5a1606" opacity="0.6"/>
    <polygon points="530,0 848,0 848,80" fill="#140603"/>
  </svg>

  <div class="instrument-art" role="img" aria-label="Two sunburst electric guitars standing in front of a guitar amplifier"></div>

  <p class="event-details">Event location, Date &amp; Time</p>

  <section class="lineup-card">
    <div class="group">
      <p class="headliner">Band Names</p>
      <p class="support">Band Names</p>
      <p class="support">Band Names</p>
    </div>
    <div class="group">
      <p class="headliner">DJ Names</p>
      <p class="support">DJ Names</p>
      <p class="support">DJ Names</p>
    </div>
  </section>

  <section class="sponsor-band">
    <p>Sponsor Names<br>and Logos</p>
  </section>

  <div class="title-strip"></div>

  <svg class="festival-title" viewBox="0 0 848 1200" role="heading" aria-level="1" aria-label="Counter-Lanternweek">
    <text class="prefix" x="22" y="992">Counter</text>
    <g class="strike">
      <line x1="420" y1="850" x2="500" y2="1010"/>
      <line x1="500" y1="850" x2="420" y2="1010"/>
    </g>
    <text class="name" x="24" y="1184" textLength="802" lengthAdjust="spacingAndGlyphs">Lanternweek</text>
  </svg>
</main>
</body>
</html>
```